Book Cover- KEEPSAKES Coming of Age near Tallow Creek, Nebraska: One Quiet Prairie River Hamlet

Lantern Field Publishing is publishing a book
Book Title: KEEPSAKES Coming of Age near Tallow Creek, Nebraska
Subtitle: One Quiet Prairie River Hamlet
Author: Dana Whitcombe
This is a serious of stories and reflections of the author's experiences growing up in small town called Tallow Creek, Colorado.

Front Cover Brief: We would like to have the first picture uploaded below - picture of mountains with fireworks included in the front cover design
Please include
Author Name: Dana Whitcombe

Back Cover Brief: The second image of the road included in the back cover design.
Please include the text- by: Dana Whitcombe.
Along with this text:

Tallow Creek is miraculous. Being touched by the magic of this beautiful place is my motivation to share the experience.

I was blessed to grow up in a beautiful town and was raised by a loving family during an amazing time of global change. Shared experiences are an exceptional way for us all to learn, grow, and be entertained. I hope you enjoy the stories as much as I enjoyed writing them. After all, the name of Tallow Creek could well be “Magic.”

This book is a collection of memories and shared experiences from growing up with friends and family in One Quiet Prairie River Hamlet. These recollections were written from a place in my heart where love lives. I loved growing up in Tallow Creek.

KEEPSAKES Coming Of Age Near Tallow Creek, Nebraska, is my effort to encourage others to reflect and share their experiences of growing up, wherever that may have been.

If space allows include the name of the publishing company: Lantern Field Publishing on back cover

Spine - We also need a spine with the title of the book Coming of Age near Tallow Creek, Nebraska : One Quiet PRAIRIE River Hamlet and Author's name - Dana Whitcombe.

```html
<!DOCTYPE html>
<html lang="en">
<head>
<meta charset="utf-8">
<title>KEEPSAKES Coming of Age near Tallow Creek, Nebraska — Cover Wrap</title>
<link rel="stylesheet" href="https://fonts.googleapis.com/css2?family=Cinzel:wght@400&family=Marcellus&family=Great+Vibes&family=Source+Sans+3:wght@400;600&display=swap">
<style>
  :root {
    --backdrop: #d9c3a6;
    --sky-top: #7ea7d8;
    --sky-mid: #6f9fd6;
    --sky-low: #8fbde6;
    --ink-white: #ffffff;
    --spine-paper: #f7f7f5;
    --spine-ink: #56616e;
    --mount-rock: #6a5560;
    --mount-forest: #233a2c;
    --glow: #e7a44a;
    --road-mist: #cfe4ef;
    --road-asphalt: #4b5258;
    --road-hill: #3f6a8c;
  }
  * { margin: 0; padding: 0; box-sizing: border-box; }
  html, body { width: 857px; height: 1200px; overflow: hidden; }
  body {
    background: linear-gradient(180deg, #e5d4bd 0%, var(--backdrop) 100%);
    position: relative;
  }
  .cover-wrap {
    position: absolute;
    left: 22px; top: 310px;
    width: 812px; height: 580px;
    display: flex;
    box-shadow: 0 10px 24px rgba(60, 40, 20, 0.3);
  }
  .panel {
    position: relative;
    width: 385px; height: 100%;
    background: linear-gradient(180deg, var(--sky-top) 0%, var(--sky-mid) 45%, var(--sky-low) 70%);
    overflow: hidden;
    color: var(--ink-white);
    text-align: center;
  }
  .author {
    font-family: "Cinzel", serif;
    letter-spacing: 0.42em;
    text-transform: uppercase;
    white-space: nowrap;
  }
  .title-main { font-family: "Marcellus", serif; line-height: 1; }
  .title-mid { font-family: "Marcellus", serif; line-height: 1; margin-top: 4px; }
  .title-script { font-family: "Great Vibes", cursive; line-height: 1.1; }
  .subtitle { font-family: "Marcellus", serif; text-transform: uppercase; }

  /* Front */
  .front .title-block { position: absolute; top: 40px; left: 0; right: 0; }
  .front .author { font-size: 12px; }
  .front .title-main { font-size: 46px; margin-top: 12px; }
  .front .title-mid { font-size: 26px; }
  .front .title-script { font-size: 25px; margin-top: 4px; }
  .front .subtitle { font-size: 10.5px; margin-top: 12px; }
  .photo-mountain {
    position: absolute; left: 0; right: 0; bottom: 0; height: 311px;
    background:
      radial-gradient(ellipse 18% 22% at 62% 30%, rgba(231,164,74,0.85), rgba(231,164,74,0) 70%),
      linear-gradient(180deg, rgba(111,159,214,0) 0%, var(--mount-rock) 28%, #7a5a55 55%, var(--mount-forest) 85%);
  }

  /* Back */
  .back .title-block { position: absolute; top: 40px; left: 0; right: 0; }
  .back .author { font-size: 8.5px; }
  .back .title-main { font-size: 33px; margin-top: 10px; }
  .back .title-mid { font-size: 18px; margin-top: 3px; }
  .back .title-script { font-size: 17px; margin-top: 2px; }
  .back .subtitle { font-size: 6.5px; margin-top: 8px; }
  .blurb {
    position: absolute; top: 192px; left: 74px; right: 74px;
    font-family: "Source Sans 3", sans-serif;
    font-size: 7.6px; line-height: 1.45;
    text-align: justify;
  }
  .blurb p + p { margin-top: 8px; }
  .blurb strong { font-weight: 600; }
  .photo-road {
    position: absolute; left: 0; right: 0; bottom: 0; height: 212px;
    background:
      linear-gradient(180deg, rgba(143,189,230,0) 0%, var(--road-hill) 30%, var(--road-mist) 55%, #b9c7a8 68%, var(--road-asphalt) 85%, #3a4046 100%);
  }

  /* Spine */
  .spine {
    width: 42px; height: 100%;
    background: var(--spine-paper);
    color: var(--spine-ink);
    writing-mode: vertical-rl;
    display: flex; align-items: center;
    padding: 24px 0;
    gap: 16px;
  }
  .spine .author { font-size: 7.5px; letter-spacing: 0.42em; }
  .spine .title-main { font-size: 12px; letter-spacing: 0.08em; white-space: nowrap; }
  .spine .title-script { font-size: 12.5px; white-space: nowrap; }
  .spine .subtitle { font-size: 4.5px; line-height: 1.3; text-align: center; }
</style>
</head>
<body>
  <div class="cover-wrap">
    <section class="panel back">
      <div class="title-block">
        <div class="author">Dana Whitcombe</div>
        <div class="title-main">KEEPSAKES</div>
        <div class="title-mid">COMING OF AGE</div>
        <div class="title-script">near Tallow Creek, Nebraska</div>
        <div class="subtitle">One Quiet Prairie River Hamlet</div>
      </div>
      <div class="blurb">
        <p>Tallow Creek is miraculous. Being touched by the magic of this beautiful place is my motivation to share the experience.</p>
        <p>I was blessed to grow up in a beautiful town and was raised by a loving family during an amazing time of global change. Shared experiences are an exceptional way for us all to learn, grow, and be entertained. I hope you enjoy the stories as much as I enjoyed writing them. After all, the name Tallow Creek could well mean “Magic.”</p>
        <p>This book is a collection of memories and shared experiences from growing up with friends and family in One Quiet Prairie River Hamlet. These recollections were written from a place in my heart where love lives. I loved growing up in Tallow Creek.</p>
        <p><strong>KEEPSAKES Coming Of Age Near Tallow Creek, Nebraska,</strong> is my effort to encourage others to reflect and share their experiences of growing up, wherever that may have been.</p>
      </div>
      <div class="photo-road" role="img" aria-label="Photograph of a two-lane road running through frosty fields toward misty blue mountains, a car ahead"></div>
    </section>

    <section class="spine">
      <div class="author">Dana Whitcombe</div>
      <div class="title-main">KEEPSAKES COMING OF AGE</div>
      <div class="title-script">near Tallow Creek, Nebraska</div>
      <div class="subtitle">ONE QUIET PRAIRIE<br>RIVER HAMLET</div>
    </section>

    <section class="panel front">
      <div class="title-block">
        <div class="author">Dana Whitcombe</div>
        <div class="title-main">KEEPSAKES</div>
        <div class="title-mid">COMING OF AGE</div>
        <div class="title-script">near Tallow Creek, Nebraska</div>
        <div class="subtitle">One Quiet Prairie River Hamlet</div>
      </div>
      <div class="photo-mountain" role="img" aria-label="Photograph of a mountain valley town at dusk with red cliffs, forested slopes and golden fireworks bursting against a snowy peak"></div>
    </section>
  </div>
</body>
</html>
```